Lakeshore Grain Corporate Powerpoint Template

We need a standardized corporate PowerPoint template that can be used for employees to create presentations with for events, meetings, and trainings. Our logo is blue, red, and white. I would like to feature the logo on each page and I visualize the "title page" to be navy blue based and "scream" Lakeshore Grain Company. I do not want the slide pages they use for content to be too busy, but still visually pleasing.

```html
<!DOCTYPE html>
<html lang="en">
<head>
<meta charset="utf-8">
<title>Lakeshore Grain Company – Corporate Presentation Template</title>
<link href="https://fonts.googleapis.com/css2?family=Poppins:ital,wght@0,400;0,500;0,600;0,700;0,800;1,500&family=Anton&display=swap" rel="stylesheet">
<style>
:root{
  --navy:#2c4597;
  --navy-dark:#223a84;
  --red:#e0323e;
  --ink:#1f1f24;
  --muted:#8a8a90;
  --grey-bar:#8b8d8f;
  --stage:#e8e9eb;
  --white:#ffffff;
}
*{box-sizing:border-box;margin:0;padding:0}
html,body{width:1046px;height:1200px;overflow:hidden}
body{background:var(--stage);font-family:'Poppins',sans-serif;color:var(--ink);position:relative}
.slide{position:absolute;width:309px;height:174px;background:var(--white);overflow:hidden;box-shadow:0 2px 6px rgba(0,0,0,.18)}
.c1{left:40px}.c2{left:369px}.c3{left:698px}
.r1{top:42px}.r2{top:232px}.r3{top:422px}.r4{top:613px}.r5{top:804px}.r6{top:998px}
.abs{position:absolute}
.photo{position:absolute}
.brand{position:absolute;right:7px;top:7px;display:flex;align-items:center;gap:2px;font-size:4.4px;font-weight:700;color:var(--navy);letter-spacing:.2px;text-transform:uppercase}
.brand i{display:block;width:4px;height:4px;background:var(--red)}
.title{position:absolute;left:9px;top:5px;font-size:10.5px;font-weight:600;color:var(--ink)}
.rule{position:absolute;left:9px;top:20px;width:22px;height:1.6px;background:linear-gradient(90deg,var(--navy) 0 70%,transparent 70% 78%,var(--red) 78%)}
.foot{position:absolute;left:13px;top:157px;width:262px;height:5px;background:var(--navy);clip-path:polygon(1.5% 0,100% 0,98.5% 100%,0 100%);color:#fff;font-size:2.4px;letter-spacing:.5px;display:flex;align-items:center;justify-content:center;gap:4px}
.pg{position:absolute;left:279px;top:157px;width:16px;height:5px;background:var(--red);clip-path:polygon(20% 0,100% 0,80% 100%,0 100%);color:#fff;font-size:2.6px;display:flex;align-items:center;justify-content:center}
.tiny{font-size:2.9px;line-height:1.35;color:var(--muted)}
.h-red{color:var(--red);font-weight:600}
.h-navy{color:var(--navy);font-weight:600}
.navy-bg{background:var(--navy)}
.logo-box{position:absolute;border:1.6px solid #fff;background:var(--navy);color:#fff;font-weight:700;text-align:center;text-transform:uppercase;display:flex;align-items:center;justify-content:center;line-height:1.1}
/* slide 1 */
.cover{background:linear-gradient(160deg,#3654a8,#2b4597 55%,#273f8b)}
.cover .stripe{position:absolute;left:0;top:145px;width:309px;height:1.4px;background:var(--red)}
.pill{position:absolute;left:71px;top:137px;width:167px;height:18px;border-radius:9px;background:var(--red);color:#fff;font-size:9.4px;font-weight:600;display:flex;align-items:center;justify-content:center}
/* slide 2 */
.big{font-family:'Anton','Poppins',sans-serif;color:var(--navy);font-size:24px;letter-spacing:.3px}
/* agenda */
.agenda-item{position:absolute;left:141px;width:120px}
.agenda-item b{font-size:5.4px;color:var(--navy);font-weight:600}
.agenda-item b span{color:var(--red)}
/* cards */
.card{position:absolute;top:73px;width:53px;height:67px;background:#fff;box-shadow:0 1px 3px rgba(0,0,0,.2);padding:12px 3px 2px}
.card .cap{position:absolute;left:0;top:-4px;width:53px;height:13px;background:var(--navy);color:#fff;font-size:7.4px;font-weight:600;display:flex;align-items:center;justify-content:center}
/* step boxes */
.pbox{position:absolute;top:36px;width:54px;height:80px;border:2px solid var(--navy);border-radius:5px;padding:30px 3px 0;text-align:center}
.pbox b{display:block;font-size:4.8px;color:var(--red);font-weight:600;margin-bottom:2px}
.numtag{display:inline-block;width:8px;height:8px;background:var(--navy);color:#fff;font-size:5.5px;font-weight:700;text-align:center;line-height:8px;margin-right:3px}
.numtag.red{background:var(--red)}.numtag.grey{background:var(--grey-bar)}
.proj{position:absolute;left:182px;width:95px}
.proj b{font-size:5.3px;font-weight:600;color:var(--ink)}
.red-dot{position:absolute;width:20px;height:20px;border-radius:50%;background:var(--red);display:flex;align-items:center;justify-content:center}
.redbtn{position:absolute;left:69px;width:86px;height:20px;background:var(--red);color:#fff;font-size:7.3px;font-weight:600;display:flex;align-items:center;padding-left:10px;box-shadow:0 1px 3px rgba(0,0,0,.25)}
.phone{position:absolute;border:1.4px solid #444;border-radius:5px;background:#fff;padding:14px 4px 4px}
.phone:before{content:"";position:absolute;left:35%;top:2px;width:30%;height:1.6px;border-radius:1px;background:#444}
.phone b{display:block;font-size:4.8px;font-weight:500;line-height:1.2;color:var(--ink)}
.member{position:absolute;top:58px;width:42px;text-align:center}
.member .hd{height:18px;margin:0 auto}
.member .av{width:23px;height:23px;border-radius:50%;border:1.5px solid #fff;margin:-13px auto 3px;background:linear-gradient(#cfd3da,#9ba2ad)}
.member b{display:block;font-size:5px;font-weight:600;margin-bottom:2px}
</style>
</head>
<body>

<!-- 1 Cover -->
<section class="slide c1 r1 cover">
  <div class="photo" role="img" aria-label="Faded farm harvester field background" style="inset:0;background:radial-gradient(ellipse at 60% 30%,rgba(255,255,255,.08),transparent 60%)"></div>
  <div class="logo-box" style="left:106px;top:62px;width:98px;height:50px;font-size:9px">Lakeshore<br>Grain</div>
  <div class="stripe"></div>
  <div class="pill">Company Business Marketing</div>
</section>

<!-- 2 Business Marketing -->
<section class="slide c2 r1">
  <div class="abs" style="left:7px;top:7px;width:7px;height:7px;background:var(--red)"></div>
  <div class="abs" style="left:20px;top:26px;width:47px;height:32px;border:1.4px solid var(--navy);color:var(--navy);font-size:6.4px;font-weight:700;text-transform:uppercase;display:flex;align-items:center;justify-content:center;text-align:center;line-height:1.1">Lakeshore<br>Grain</div>
  <div class="abs big" style="left:18px;top:68px">BUSINESS</div>
  <div class="abs" style="left:18px;top:100px;font-size:11px;font-weight:600;color:var(--red);letter-spacing:.3px">MARKETING</div>
  <div class="abs" style="left:18px;top:118px;width:14px;height:1.5px;background:var(--navy)"></div>
  <div class="abs" style="left:34px;top:118px;width:3px;height:1.5px;background:var(--red)"></div>
  <div class="abs" style="left:18px;top:123px;font-size:7.6px;font-style:italic;font-weight:500;color:var(--navy)">Presentation</div>
  <div class="abs tiny" style="left:18px;top:134px;width:82px;font-style:italic">Lorem ipsum dolor sit amet, consectetuer adipiscing elit, sed diam nonum</div>
  <div class="abs" style="left:19px;top:157px;display:flex;gap:3px"><i style="width:3px;height:3px;border-radius:50%;background:var(--navy)"></i><i style="width:3px;height:3px;border-radius:50%;background:var(--red)"></i><i style="width:3px;height:3px;border-radius:50%;background:var(--navy)"></i></div>
  <div class="photo" role="img" aria-label="Harvester loading sugar beets under blue sky" style="left:130px;top:0;width:179px;height:142px;background:linear-gradient(180deg,#7fa8dc 0%,#b7cde6 38%,#a38c62 62%,#8a7555 100%)"></div>
  <div class="abs navy-bg" style="left:130px;top:142px;width:179px;height:32px;color:#fff;font-size:6px;letter-spacing:2px;display:flex;align-items:center;justify-content:center">WWW.WEBSITE.COM</div>
</section>

<!-- 3 Agenda -->
<section class="slide c3 r1">
  <div class="brand"><i></i>Lakeshore Grain</div>
  <div class="abs" style="left:41px;top:72px;width:3px;height:26px;background:var(--red)"></div>
  <div class="abs" style="left:48px;top:70px;font-size:18px;font-weight:600">Agenda</div>
  <div class="agenda-item" style="top:32px"><b><span>1.</span> Lorem ipsum</b><p class="tiny">Lorem ipsum dolor sit amet, consectetuer adipiscing elit, sed diam nonummy nibh euismod tincid</p></div>
  <div class="agenda-item" style="top:60px"><b style="color:var(--red)">2. Lorem ipsum</b><p class="tiny">Lorem ipsum dolor sit amet, consectetuer adipiscing elit, sed diam nonummy nibh euismod tincid</p></div>
  <div class="agenda-item" style="top:88px"><b><span>3.</span> Lorem ipsum</b><p class="tiny">Lorem ipsum dolor sit amet, consectetuer adipiscing elit, sed diam nonummy nibh euismod tincid</p></div>
  <div class="agenda-item" style="top:115px"><b style="color:var(--red)">4. Lorem ipsum</b><p class="tiny">Lorem ipsum dolor sit amet, consectetuer adipiscing elit, sed diam nonummy nibh euismod tincid</p></div>
  <div class="foot"><span>© Copyright 2024</span>|<span>Lakeshore Grain Company</span>|<span>All Rights Reserved</span></div><div class="pg">2</div>
</section>

<!-- 4 Text Added Here cards -->
<section class="slide c1 r2">
  <div class="brand"><i></i>Lakeshore Grain</div>
  <div class="abs" style="left:0;top:30px;width:9px;height:70px;background:var(--red)"></div>
  <div class="abs" style="left:17px;top:29px;font-size:18px;font-weight:700;line-height:1.35">Text<br>Added<br>Here</div>
  <div class="photo" role="img" aria-label="Yellow harvester in a green field" style="left:98px;top:28px;width:211px;height:70px;background:linear-gradient(180deg,#6f9ad4 0%,#a9c4e4 30%,#c9a832 55%,#5d8a3a 100%)"></div>
  <div class="card" style="left:110px"><div class="cap">Text Here</div><p class="tiny">Lorem ipsum dolor sit amet, consectetuer adipiscing elit, sed diam nonummy nibh euismod tincidunt ut laoreet dolore magna aliquam erat volutpat.<br><br>Ut wisi enim ad minim veniam, quis nostrud exerci tation ullamcorper</p></div>
  <div class="card" style="left:177px"><div class="cap">Text Here</div><p class="tiny">Lorem ipsum dolor sit amet, consectetuer adipiscing elit, sed diam nonummy nibh euismod tincidunt ut laoreet dolore magna aliquam erat volutpat.<br><br>Ut wisi enim ad minim veniam, quis nostrud exerci tation ullamcorper</p></div>
  <div class="card" style="left:244px"><div class="cap">Text Here</div><p class="tiny">Lorem ipsum dolor sit amet, consectetuer adipiscing elit, sed diam nonummy nibh euismod tincidunt ut laoreet dolore magna aliquam erat volutpat.<br><br>Ut wisi enim ad minim veniam, quis nostrud exerci tation ullamcorper</p></div>
  <div class="foot"><span>© Copyright 2024</span>|<span>Lakeshore Grain Company</span>|<span>All Rights Reserved</span></div><div class="pg">3</div>
</section>

<!-- 5 Idea / Promotion / Growth -->
<section class="slide c2 r2">
  <div class="title">Text Added Here</div><div class="rule"></div>
  <div class="brand"><i></i>Lakeshore Grain</div>
  <div class="photo" role="img" aria-label="Faint world map backdrop" style="left:40px;top:25px;width:230px;height:100px;background:radial-gradient(ellipse,#f1f2f4 30%,transparent 70%)"></div>
  <div class="pbox" style="left:60px"><b>IDEA</b><p class="tiny">Lorem ipsum dolor sit amet, consectetuer adipiscing elit, sed diam nonummy nibh euismod tincidunt ut laoreet dolore</p></div>
  <div class="pbox" style="left:131px"><b>PROMOTION</b><p class="tiny">Lorem ipsum dolor sit amet, consectetuer adipiscing elit, sed diam nonummy nibh euismod tincidunt ut laoreet dolore</p></div>
  <div class="pbox" style="left:202px"><b>GROWTH</b><p class="tiny">Lorem ipsum dolor sit amet, consectetuer adipiscing elit, sed diam nonummy nibh euismod tincidunt ut laoreet dolore</p></div>
  <svg class="abs" style="left:0;top:0" width="309" height="174" viewBox="0 0 309 174">
    <g fill="none" stroke="var(--navy)" stroke-width="1.4">
      <circle cx="87" cy="54" r="3.5"/><path d="M87 58v3M85.5 62h3"/>
      <rect x="152" y="50" width="12" height="8"/><path d="M152 50l6 5 6-5"/>
      <path d="M223 50v9h11M225 57l3-3 2 2 4-4"/>
    </g>
    <g fill="var(--navy)"><circle cx="111" cy="60" r="2.8"/><circle cx="132" cy="108" r="2.8"/><circle cx="182" cy="60" r="2.8"/><circle cx="203" cy="108" r="2.8"/></g>
  </svg>
  <p class="abs tiny" style="left:40px;top:126px;width:230px;text-align:center">Lorem ipsum dolor sit amet, consectetuer adipiscing elit, sed diam nonummy nibh euismod tincidunt ut laoreet dolore magna aliquam erat volutpat. Ut wisi enim ad minim veniam, quis nostrud exerci tation ullamcorper suscipit lobortis nisl ut aliquip ex ea commodo consequat.</p>
  <div class="foot"><span>© Copyright 2024</span>|<span>Lakeshore Grain Company</span>|<span>All Rights Reserved</span></div><div class="pg">4</div>
</section>

<!-- 6 List + blue panel -->
<section class="slide c3 r2">
  <div class="title">Text Added Here</div><div class="rule"></div>
  <div class="brand"><i></i>Lakeshore Grain</div>
  <div class="abs" style="left:38px;top:41px;width:102px"><b class="h-navy" style="font-size:4.4px"><span style="color:var(--red)">01.</span> Aliquam Erat Volutpat</b><p class="tiny" style="padding-left:8px">Lorem ipsum dolor sit amet, consectetuer adipiscing elit, sed diam nonummy nibh euismod</p></div>
  <div class="abs" style="left:38px;top:67px;width:102px"><b class="h-navy" style="font-size:4.4px"><span style="color:var(--red)">02.</span> Consectetuer Adipiscing Elit</b><p class="tiny" style="padding-left:8px">Lorem ipsum dolor sit amet, consectetuer adipiscing elit, sed diam nonummy nibh euismod tincidunt</p></div>
  <div class="abs" style="left:38px;top:94px;width:102px"><b class="h-navy" style="font-size:4.4px"><span style="color:var(--red)">03.</span> Duis Autem Vel Eum</b><p class="tiny" style="padding-left:8px">Lorem ipsum dolor sit amet, consectetuer adipiscing elit, sed diam nonummy nibh euismod tincidunt</p></div>
  <div class="abs" style="left:38px;top:120px;width:102px"><b class="h-navy" style="font-size:4.4px"><span style="color:var(--red)">04.</span> Aliquam Erat Volutpat</b><p class="tiny" style="padding-left:8px">Lorem ipsum dolor sit amet, consectetuer adipiscing elit, sed diam nonummy nibh euismod tincidunt</p></div>
  <div class="abs navy-bg" style="left:165px;top:38px;width:99px;height:102px"></div>
  <div class="red-dot" style="left:154px;top:50px;border:2px solid #fff"></div>
  <div class="red-dot" style="left:154px;top:80px;border:2px solid #fff"></div>
  <div class="red-dot" style="left:154px;top:112px;border:2px solid #fff"></div>
  <div class="abs" style="left:183px;top:48px;width:76px;color:#fff"><b style="font-size:5.6px;font-weight:500">Lorem ipsum</b><p class="tiny" style="color:#dfe4f3">ipsum dolor sit amet, cons ectetuer adipiscing elit, sed diam nonummy</p></div>
  <div class="abs" style="left:183px;top:78px;width:76px;color:#fff"><b style="font-size:5.6px;font-weight:500">Lorem ipsum</b><p class="tiny" style="color:#dfe4f3">ipsum dolor sit amet, cons ectetuer adipiscing elit, sed diam nonummy</p></div>
  <div class="abs" style="left:183px;top:110px;width:76px;color:#fff"><b style="font-size:5.6px;font-weight:500">Lorem ipsum</b><p class="tiny" style="color:#dfe4f3">ipsum dolor sit amet, cons ectetuer adipiscing elit, sed diam nonummy</p></div>
  <div class="foot"><span>© Copyright 2024</span>|<span>Lakeshore Grain Company</span>|<span>All Rights Reserved</span></div><div class="pg">5</div>
</section>

<!-- 7 Bar chart -->
<section class="slide c1 r3">
  <div class="title">Text Added Here</div><div class="rule"></div>
  <div class="brand"><i></i>Lakeshore Grain</div>
  <div class="abs" style="left:18px;top:47px;width:75px"><span class="numtag">1.</span><b class="h-navy" style="font-size:5.4px">Lorem ipsum</b><p class="tiny" style="padding-left:25px;margin-top:-3px">Lorem ipsum dolor sit amet, consectetuer adipiscing elit, sed diam nonummy</p></div>
  <div class="abs" style="left:18px;top:79px;width:75px"><span class="numtag red">2.</span><b class="h-red" style="font-size:5.4px">Lorem ipsum</b><p class="tiny" style="padding-left:25px;margin-top:-3px">Lorem ipsum dolor sit amet, consectetuer adipiscing elit, sed diam nonummy</p></div>
  <div class="abs" style="left:18px;top:111px;width:75px"><span class="numtag grey">3.</span><b style="font-size:5.4px;font-weight:600;color:var(--grey-bar)">Lorem ipsum</b><p class="tiny" style="padding-left:25px;margin-top:-3px">Lorem ipsum dolor sit amet, consectetuer adipiscing elit, sed diam nonummy</p></div>
  <svg class="abs" style="left:0;top:0" width="309" height="174" viewBox="0 0 309 174" font-family="Poppins,sans-serif" font-size="4.4" fill="#333" text-anchor="middle">
    <line x1="102" y1="128" x2="288" y2="128" stroke="#ddd" stroke-width=".5"/>
    <!-- group 1 -->
    <rect x="114" y="65.6" width="4.5" height="62.4" fill="var(--navy)"/><text x="116" y="63">43%</text>
    <rect x="123" y="93.2" width="4.5" height="34.8" fill="var(--red)"/><text x="125" y="91">24%</text>
    <rect x="132" y="99" width="4.5" height="29" fill="var(--grey-bar)"/><text x="135" y="97">20%</text>
    <!-- group 2 -->
    <rect x="160" y="91.8" width="4.5" height="36.2" fill="var(--navy)"/><text x="162" y="89.5">25%</text>
    <rect x="169" y="64.2" width="4.5" height="63.8" fill="var(--red)"/><text x="171" y="62">44%</text>
    <rect x="178" y="99" width="4.5" height="29" fill="var(--grey-bar)"/><text x="181" y="97">20%</text>
    <!-- group 3 -->
    <rect x="206" y="77.2" width="4.5" height="50.8" fill="var(--navy)"/><text x="208" y="75">35%</text>
    <rect x="215" y="101.9" width="4.5" height="26.1" fill="var(--red)"/><text x="217" y="99.5">18%</text>
    <rect x="224" y="84.5" width="4.5" height="43.5" fill="var(--grey-bar)"/><text x="227" y="82">30%</text>
    <!-- group 4 -->
    <rect x="252" y="62.8" width="4.5" height="65.2" fill="var(--navy)"/><text x="254" y="60.5">45%</text>
    <rect x="261" y="87.4" width="4.5" height="40.6" fill="var(--red)"/><text x="263" y="85">28%</text>
    <rect x="270" y="55.5" width="4.5" height="72.5" fill="var(--grey-bar)"/><text x="273" y="53">50%</text>
    <text x="125" y="135">1</text><text x="171" y="135">2</text><text x="217" y="135">3</text><text x="263" y="135">4</text>
    <g font-size="3.4" text-anchor="start"><rect x="167" y="140" width="2" height="2" fill="var(--navy)"/><text x="170" y="142">Series1</text><rect x="187" y="140" width="2" height="2" fill="var(--red)"/><text x="190" y="142">Series2</text><rect x="207" y="140" width="2" height="2" fill="var(--grey-bar)"/><text x="210" y="142">Series3</text></g>
  </svg>
  <div class="foot"><span>© Copyright 2024</span>|<span>Lakeshore Grain Company</span>|<span>All Rights Reserved</span></div><div class="pg">6</div>
</section>

<!-- 8 Part One -->
<section class="slide c2 r3">
  <div class="abs navy-bg" style="left:0;top:54px;width:11px;height:43px"></div>
  <div class="abs" style="left:22px;top:58px;font-size:15px;font-weight:700">Part One</div>
  <p class="abs tiny" style="left:22px;top:78px;width:95px">Lorem ipsum dolor sit amet, laoreet dolore magna aliquam erat volutpat. Ut wisi it lob edo consequat. Duis autem lore te feugait nulla facilisi.</p>
  <p class="abs tiny" style="left:22px;top:98px;width:95px">Lorem ipsum dolor sit amet, cons ectetuer adipiscing elit, sed diam nonim ad minim veniam, quis nostrud exerci tation ullamcorper</p>
  <div class="abs navy-bg" style="left:224px;top:117px;width:85px;height:57px"></div>
  <div class="photo" role="img" aria-label="Storage silo beside a pile of sugar beets" style="left:162px;top:15px;width:129px;height:143px;background:linear-gradient(180deg,#4f86d6 0%,#9fbfe8 35%,#c9c9c4 50%,#a88e6a 72%,#7c6446 100%)"></div>
  <div class="abs" style="left:126px;top:52px;width:69px;height:69px;background:var(--red);color:#fff;font-family:'Anton','Poppins',sans-serif;font-size:44px;display:flex;align-items:center;justify-content:center">01</div>
</section>

<!-- 9 Photo + list -->
<section class="slide c3 r3">
  <div class="title">Text Added Here</div><div class="rule"></div>
  <div class="brand"><i></i>Lakeshore Grain</div>
  <div class="photo" role="img" aria-label="Worker holding a machine part" style="left:28px;top:36px;width:87px;height:105px;background:linear-gradient(160deg,#b89a6e,#7d6a52 55%,#4a4a48)"></div>
  <div class="abs" style="left:129px;top:42px;width:140px"><b class="h-red" style="font-size:6.2px">1. Text Added Here</b><p class="tiny">Lorem ipsum dolor sit amet, cons ectetuer adipiscing elit, sed diam nonummy nibh euismod tincidunt ut laoreet dolore magna aliquam erat volutpat.</p></div>
  <div class="abs" style="left:129px;top:76px;width:140px"><b class="h-red" style="font-size:6.2px">2. Text Added Here</b><p class="tiny">Lorem ipsum dolor sit amet, cons ectetuer adipiscing elit, sed diam nonummy nibh euismod tincidunt ut laoreet dolore magna aliquam erat volutpat.</p></div>
  <div class="abs" style="left:129px;top:111px;width:140px"><b class="h-red" style="font-size:6.2px">3. Text Added Here</b><p class="tiny">Lorem ipsum dolor sit amet, cons ectetuer adipiscing elit, sed diam nonummy nibh euismod tincidunt ut laoreet dolore magna aliquam erat volutpat.</p></div>
  <div class="foot"><span>© Copyright 2024</span>|<span>Lakeshore Grain Company</span>|<span>All Rights Reserved</span></div><div class="pg">8</div>
</section>

<!-- 10 Circle + projects -->
<section class="slide c1 r4">
  <div class="title">Text Added Here</div><div class="rule"></div>
  <div class="brand"><i></i>Lakeshore Grain</div>
  <svg class="abs" style="left:0;top:0" width="309" height="174" viewBox="0 0 309 174">
    <circle cx="77" cy="88" r="34" fill="none" stroke="var(--navy)" stroke-width="2.4"/>
    <circle cx="77" cy="88" r="30" fill="none" stroke="var(--navy)" stroke-width=".6"/>
    <g fill="none" stroke="var(--navy)" stroke-width=".8"><path d="M112 68l11-16h23M113 88h33M112 108l11 16h23"/></g>
    <g fill="var(--red)"><circle cx="164" cy="52" r="11"/><circle cx="164" cy="88" r="11"/><circle cx="164" cy="124" r="11"/></g>
    <g fill="none" stroke="#fff" stroke-width=".9"><circle cx="164" cy="52" r="5"/><circle cx="164" cy="52" r="2"/><circle cx="164" cy="88" r="5"/><circle cx="164" cy="88" r="2"/><circle cx="164" cy="124" r="5"/><circle cx="164" cy="124" r="2"/></g>
  </svg>
  <div class="abs" style="left:43px;top:76px;width:68px;text-align:center;font-size:8.4px;font-weight:600;line-height:1.25">Add<br>Text Here</div>
  <div class="proj" style="top:42px"><b>Project name</b><p class="tiny">Lorem ipsum dolor sit amet, nec an dictas equidem appellantur, ut has commune accommodare. Mea illum, ludus soleat idpro.</p></div>
  <div class="proj" style="top:78px"><b>Project name</b><p class="tiny">Lorem ipsum dolor sit amet, nec an dictas equidem appellantur, ut has commune accommodare. Mea illum, ludus soleat idpro.</p></div>
  <div class="proj" style="top:114px"><b>Project name</b><p class="tiny">Lorem ipsum dolor sit amet, nec an dictas equidem appellantur, ut has commune accommodare. Mea illum, ludus soleat idpro.</p></div>
  <div class="foot"><span>© Copyright 2024</span>|<span>Lakeshore Grain Company</span>|<span>All Rights Reserved</span></div><div class="pg">9</div>
</section>

<!-- 11 Three options -->
<section class="slide c2 r4">
  <div class="title">Text Added Here</div><div class="rule"></div>
  <div class="brand"><i></i>Lakeshore Grain</div>
  <svg class="abs" style="left:26px;top:72px" width="34" height="34" viewBox="0 0 34 34"><path d="M2 0h14l16 17-16 17H2l16-17z" fill="#e6e6e8"/></svg>
  <div class="photo" role="img" aria-label="Speaker at a podium" style="left:77px;top:36px;width:54px;height:64px;background:linear-gradient(160deg,#3b4f8a,#1c2440 60%,#6b5d53)"></div>
  <div class="photo" role="img" aria-label="Industrial factory building" style="left:148px;top:36px;width:54px;height:64px;background:linear-gradient(180deg,#6d96d8,#a8b3c0 45%,#6a6e74)"></div>
  <div class="photo" role="img" aria-label="Group of staff at an event" style="left:218px;top:36px;width:54px;height:64px;background:linear-gradient(180deg,#d7d7d7,#9b6a5d 50%,#4b4a55)"></div>
  <div class="abs" style="left:77px;top:103px;width:56px"><b style="font-size:5px;font-weight:500;color:var(--red)">First <span class="h-navy">Option</span></b><p class="tiny">Lorem ipsum dolor sit consectetuer adipiscing elit, sed diam nonummy nibh euismod tincidunt ut dolore magna aliquam erat volutpat.</p></div>
  <div class="abs" style="left:148px;top:103px;width:56px"><b style="font-size:5px;font-weight:500;color:var(--red)">Second <span class="h-navy">Option</span></b><p class="tiny">Lorem ipsum dolor sit consectetuer adipiscing elit, sed diam nonummy nibh euismod tincidunt ut dolore magna aliquam erat volutpat.</p></div>
  <div class="abs" style="left:218px;top:103px;width:56px"><b style="font-size:5px;font-weight:500;color:var(--red)">Third <span class="h-navy">Option</span></b><p class="tiny">Lorem ipsum dolor sit consectetuer adipiscing elit, sed diam nonummy nibh euismod tincidunt ut dolore magna aliquam erat volutpat.</p></div>
  <div class="foot"><span>© Copyright 2024</span>|<span>Lakeshore Grain Company</span>|<span>All Rights Reserved</span></div><div class="pg">10</div>
</section>

<!-- 12 Silo + buttons -->
<section class="slide c3 r4">
  <div class="brand"><i></i>Lakeshore Grain</div>
  <div class="photo" role="img" aria-label="Silo with staff group in front" style="left:27px;top:22px;width:74px;height:118px;background:linear-gradient(180deg,#d8dde6,#b9c0cc 60%,#5a6a8a 85%,#3b4a66)"></div>
  <div class="redbtn" style="top:35px">1. Lorem Ipsum</div>
  <div class="redbtn" style="top:71px">2. Lorem Ipsum</div>
  <div class="redbtn" style="top:107px">3. Lorem Ipsum</div>
  <div class="abs" style="left:173px;top:38px;font-size:12px;font-weight:600;line-height:1.2">Text<br>Added Hare</div>
  <div class="abs" style="left:173px;top:70px;width:12px;height:1.5px;background:var(--navy)"></div>
  <div class="abs" style="left:187px;top:70px;width:3px;height:1.5px;background:var(--red)"></div>
  <p class="abs" style="left:173px;top:80px;width:105px;font-size:4.3px;line-height:1.4;color:#666">Lorem ipsum dolor sit amet, consectetuer adipiscing elit, sed diam nonummy nibh .</p>
  <p class="abs" style="left:173px;top:96px;width:105px;font-size:4.3px;line-height:1.4;color:#666">Ut wisi enim ad minim veniam, quis nostrud exerci tation ullamcorper suscipit lobortis. Ut wisi enim ad minim veniam, quis nostrud exerci tation ullamcorper suscipit</p>
  <div class="foot"><span>© Copyright 2024</span>|<span>Lakeshore Grain Company</span>|<span>All Rights Reserved</span></div><div class="pg">11</div>
</section>

<!-- 13 Timeline -->
<section class="slide c1 r5">
  <div class="title">Text Added Here</div><div class="rule"></div>
  <div class="brand"><i></i>Lakeshore Grain</div>
  <svg class="abs" style="left:0;top:0" width="309" height="174" viewBox="0 0 309 174" font-family="Poppins,sans-serif" font-size="4.6" font-weight="500" text-anchor="middle">
    <g stroke-width=".9"><path d="M54 64v13" stroke="var(--navy)"/><path d="M154 64v13" stroke="var(--navy)"/><path d="M254 64v13" stroke="var(--navy)"/><path d="M104 92v12" stroke="var(--red)"/><path d="M204 92v12" stroke="var(--red)"/></g>
    <g fill="var(--navy)"><circle cx="54" cy="64" r="1.3"/><circle cx="154" cy="64" r="1.3"/><circle cx="254" cy="64" r="1.3"/></g>
    <g fill="var(--red)"><circle cx="104" cy="104" r="1.3"/><circle cx="204" cy="104" r="1.3"/></g>
    <path d="M30 86l5-8h40l-5 8z" fill="var(--navy)"/>
    <path d="M77 78h46l-5 9h-36z" fill="var(--red)"/>
    <path d="M130 86l5-8h40l-5 8z" fill="var(--navy)"/>
    <path d="M177 78h46l-5 9h-36z" fill="var(--red)"/>
    <path d="M230 86l5-8h40l5 8z" fill="var(--navy)"/>
    <g fill="#fff"><text x="54" y="84">1990</text><text x="104" y="84.5">2001</text><text x="154" y="84">2007</text><text x="204" y="84.5">2012</text><text x="254" y="84">2020</text></g>
    <g fill="#222" font-weight="600" font-size="5"><text x="54" y="48">Your Title</text><text x="154" y="48">Your Title</text><text x="254" y="48">Your Title</text><text x="104" y="119">Your Title</text><text x="204" y="119">Your Title</text></g>
    <g fill="#888" font-weight="400" font-size="3.8"><text x="54" y="53">Refers to a good or</text><text x="54" y="57.5">service being offered</text><text x="154" y="53">Refers to a good or</text><text x="154" y="57.5">service being offered</text><text x="254" y="53">Refers to a good or</text><text x="254" y="57.5">service being offered</text><text x="104" y="124">Refers to a good or</text><text x="104" y="128.5">service being offered</text><text x="204" y="124">Refers to a good or</text><text x="204" y="128.5">service being offered</text></g>
  </svg>
  <div class="foot"><span>© Copyright 2024</span>|<span>Lakeshore Grain Company</span>|<span>All Rights Reserved</span></div><div class="pg">12</div>
</section>

<!-- 14 Ring -->
<section class="slide c2 r5">
  <div class="title">Text Added Here</div><div class="rule"></div>
  <div class="brand"><i></i>Lakeshore Grain</div>
  <svg class="abs" style="left:0;top:0" width="309" height="174" viewBox="0 0 309 174">
    <g stroke="#fff" stroke-width="1.6">
      <path d="M155 43A43 43 0 0 1 198 86L177 86A22 22 0 0 0 155 64Z" fill="var(--red)"/>
      <path d="M112 86A43 43 0 0 1 155 43L155 64A22 22 0 0 0 133 86Z" fill="var(--navy)"/>
      <path d="M198 86A43 43 0 0 1 155 129L155 108A22 22 0 0 0 177 86Z" fill="var(--navy)"/>
      <path d="M155 129A43 43 0 0 1 112 86L133 86A22 22 0 0 0 155 108Z" fill="var(--red)"/>
    </g>
    <g fill="none" stroke="#fff" stroke-width=".9"><circle cx="133" cy="66" r="4"/><circle cx="177" cy="66" r="4"/><circle cx="133" cy="106" r="4"/><circle cx="177" cy="106" r="4"/></g>
  </svg>
  <div class="abs" style="left:133px;top:76px;width:44px;text-align:center;font-size:7.4px;font-weight:600;line-height:1.15">Text<br>Added</div>
  <div class="abs" style="left:32px;top:44px;width:72px;text-align:right"><b style="font-size:5.4px;font-weight:600">Text Here</b><p class="tiny">Lorem ipsum dolor sit amet, consectetuer adipiscing elit, sed diammy nibh euismod tincidunt ut laoreet dolore</p></div>
  <div class="abs" style="left:32px;top:105px;width:72px;text-align:right"><b style="font-size:5.4px;font-weight:600">Text Here</b><p class="tiny">Lorem ipsum dolor sit amet, consectetuer adipiscing elit, sed diammy nibh euismod tincidunt ut laoreet dolore</p></div>
  <div class="abs" style="left:207px;top:44px;width:72px"><b style="font-size:5.4px;font-weight:600">Text Here</b><p class="tiny">Lorem ipsum dolor sit amet, consectetuer adipiscing elit, sed diammy nibh euismod tincidunt ut laoreet dolore</p></div>
  <div class="abs" style="left:207px;top:105px;width:72px"><b style="font-size:5.4px;font-weight:600">Text Here</b><p class="tiny">Lorem ipsum dolor sit amet, consectetuer adipiscing elit, sed diammy nibh euismod tincidunt ut laoreet dolore</p></div>
  <div class="foot"><span>© Copyright 2024</span>|<span>Lakeshore Grain Company</span>|<span>All Rights Reserved</span></div><div class="pg">13</div>
</section>

<!-- 15 Steps -->
<section class="slide c3 r5">
  <div class="title">Text Added Here</div><div class="rule"></div>
  <div class="brand"><i></i>Lakeshore Grain</div>
  <svg class="abs" style="left:0;top:0" width="309" height="174" viewBox="0 0 309 174" font-family="Poppins,sans-serif" font-size="3.6" font-weight="600" text-anchor="middle">
    <path d="M24 81h134" stroke="var(--navy)" stroke-width="4"/>
    <path d="M104 81h50" stroke="var(--red)" stroke-width="4"/>
    <path d="M158 81h50" stroke="var(--navy)" stroke-width="4"/>
    <path d="M212 81h60" stroke="var(--red)" stroke-width="4"/><path d="M270 76l7 5-7 5z" fill="var(--red)"/>
    <g fill="#fff" stroke-width="3"><circle cx="75" cy="67" r="16" stroke="var(--navy)"/><circle cx="129" cy="67" r="16" stroke="var(--red)"/><circle cx="183" cy="67" r="16" stroke="var(--navy)"/><circle cx="237" cy="67" r="16" stroke="var(--red)"/></g>
    <g fill="#fff" stroke-width=".8"><circle cx="75" cy="67" r="11" stroke="var(--navy)"/><circle cx="129" cy="67" r="11" stroke="var(--red)"/><circle cx="183" cy="67" r="11" stroke="var(--navy)"/><circle cx="237" cy="67" r="11" stroke="var(--red)"/></g>
    <g fill="none" stroke-width="1"><circle cx="75" cy="67" r="5" stroke="var(--navy)"/><path d="M75 64v3l2 2" stroke="var(--navy)"/><rect x="126" y="63" width="6" height="7" rx="2" fill="var(--navy)"/><path d="M179 63h8M179 66h8M179 69h8" stroke="var(--navy)" stroke-width="1.5"/><circle cx="238" cy="65" r="3.5" stroke="var(--navy)"/><path d="M235 68l-3 3" stroke="var(--navy)"/></g>
    <g fill="#fff"><text x="89" y="82.3">Step 01</text><text x="143" y="82.3">Step 02</text><text x="197" y="82.3">Step 03</text><text x="251" y="82.3">Step 04</text></g>
    <g stroke="#999" stroke-width=".6"><path d="M75 87v8M129 87v8M183 87v8M237 87v8"/></g>
  </svg>
  <div class="abs" style="left:53px;top:100px;width:44px;text-align:center"><b style="font-size:5.6px;font-weight:600">Lorem Ipsum</b><p class="tiny">Lorem ipsum dolor sit amet, consectetuer adipiscing elit, sed diam nonummy nibh euismod tincidunt ut laoreet dolore</p></div>
  <div class="abs" style="left:107px;top:100px;width:44px;text-align:center"><b style="font-size:5.6px;font-weight:600">Lorem Ipsum</b><p class="tiny">Lorem ipsum dolor sit amet, consectetuer adipiscing elit, sed diam nonummy nibh euismod tincidunt ut laoreet dolore</p></div>
  <div class="abs" style="left:161px;top:100px;width:44px;text-align:center"><b style="font-size:5.6px;font-weight:600">Lorem Ipsum</b><p class="tiny">Lorem ipsum dolor sit amet, consectetuer adipiscing elit, sed diam nonummy nibh euismod tincidunt ut laoreet dolore</p></div>
  <div class="abs" style="left:215px;top:100px;width:44px;text-align:center"><b style="font-size:5.6px;font-weight:600">Lorem Ipsum</b><p class="tiny">Lorem ipsum dolor sit amet, consectetuer adipiscing elit, sed diam nonummy nibh euismod tincidunt ut laoreet dolore</p></div>
  <div class="foot"><span>© Copyright 2024</span>|<span>Lakeshore Grain Company</span>|<span>All Rights Reserved</span></div><div class="pg">14</div>
</section>

<!-- 16 Phones -->
<section class="slide c1 r6">
  <div class="abs" style="left:12px;top:7px;font-size:10.5px;font-weight:600">Text Added Here</div>
  <div class="abs" style="left:12px;top:22px;width:22px;height:1.6px;background:linear-gradient(90deg,var(--navy) 0 70%,transparent 70% 78%,var(--red) 78%)"></div>
  <div class="brand"><i></i>Lakeshore Grain</div>
  <p class="abs tiny" style="left:15px;top:30px;width:98px;font-size:3.4px">Lorem ipsum dolor sit amet, consectetuer adipiscing elit, sed diam nonummy nibh euismod tincidunt ut laoreet dolore magna aliquam erat volutpat. Ut wisi enim ad minim veniam,<br><br>quis nostrud exerci tation ullamcorper suscipit lobortis nisl ut aliquip ex ea commodo consequat. Duis autem vel eum iriure dolor in hendrerit in vulputate velit esse</p>
  <div class="abs" style="left:28px;top:86px;width:85px"><span class="numtag red">1.</span><b class="h-navy" style="font-size:4.6px">Lorem ipsum</b><p class="tiny" style="padding-left:13px;margin-top:-3px">Lorem ipsum dolor sit amet, consectetuer adipiscing elit, sed diam nonummy nibh euismod</p></div>
  <div class="abs" style="left:28px;top:107px;width:85px"><span class="numtag red">2.</span><b class="h-navy" style="font-size:4.6px">Lorem ipsum</b><p class="tiny" style="padding-left:13px;margin-top:-3px">Lorem ipsum dolor sit amet, consectetuer adipiscing elit, sed diam nonummy nibh euismod</p></div>
  <div class="abs" style="left:28px;top:129px;width:85px"><span class="numtag red">3.</span><b class="h-navy" style="font-size:4.6px">Lorem ipsum</b><p class="tiny" style="padding-left:13px;margin-top:-3px">Lorem ipsum dolor sit amet, consectetuer adipiscing elit, sed diam nonummy nibh euismod</p></div>
  <div class="phone" style="left:136px;top:24px;width:39px;height:81px"><b>Lorem<br>ipsum dolor</b><svg width="12" height="10" style="display:block;margin:4px auto"><path d="M1 1h5v8H1zM6 1h5v8H6z" fill="none" stroke="var(--red)" stroke-width=".8"/></svg><p class="tiny" style="font-size:2.4px">To introduce the students to the changing landscape of marketing and equip them with tools</p></div>
  <div class="phone" style="left:186px;top:42px;width:39px;height:81px"><b>Dolor sit<br>amet, conse</b><svg width="12" height="10" style="display:block;margin:4px auto"><circle cx="6" cy="5" r="4" fill="none" stroke="var(--red)" stroke-width=".8"/></svg><p class="tiny" style="font-size:2.4px">You will learn concepts and ideas in digital marketing as well as tools and strategies</p></div>
  <div class="phone" style="left:235px;top:59px;width:39px;height:81px"><b>Consec</b><svg width="12" height="10" style="display:block;margin:4px auto"><circle cx="6" cy="5" r="4" fill="none" stroke="var(--red)" stroke-width=".8"/></svg><p class="tiny" style="font-size:2.4px">You are required to pass 80% of the evaluation test to obtain the certificate</p></div>
  <div class="foot"><span>© Copyright 2024</span>|<span>Lakeshore Grain Company</span>|<span>All Rights Reserved</span></div><div class="pg">15</div>
</section>

<!-- 17 Team -->
<section class="slide c2 r6">
  <div class="abs" style="left:9px;top:6px;font-size:10.5px;font-weight:600">Text Added Here</div>
  <div class="abs" style="left:9px;top:21px;width:22px;height:1.6px;background:linear-gradient(90deg,var(--navy) 0 70%,transparent 70% 78%,var(--red) 78%)"></div>
  <div class="brand"><i></i>Lakeshore Grain</div>
  <div class="member" style="left:37px"><div class="hd navy-bg"></div><div class="av" role="img" aria-label="Team member portrait"></div><b>JOHN SMITH</b><p class="tiny">Ipsum dolor sit amet, cons ectetuer adipiscing elit, sed diam nonummy nibh euismod</p></div>
  <div class="member" style="left:100px"><div class="hd" style="background:var(--red)"></div><div class="av" role="img" aria-label="Team member portrait"></div><b>MILLIE SMITH</b><p class="tiny">Ipsum dolor sit amet, cons ectetuer adipiscing elit, sed diam nonummy nibh euismod</p></div>
  <div class="member" style="left:163px"><div class="hd navy-bg"></div><div class="av" role="img" aria-label="Team member portrait"></div><b>JOHN SMITH</b><p class="tiny">Ipsum dolor sit amet, cons ectetuer adipiscing elit, sed diam nonummy nibh euismod</p></div>
  <div class="member" style="left:227px"><div class="hd" style="background:var(--red)"></div><div class="av" role="img" aria-label="Team member portrait"></div><b>MILLIE SMITH</b><p class="tiny">Ipsum dolor sit amet, cons ectetuer adipiscing elit, sed diam nonummy nibh euismod</p></div>
  <div class="foot"><span>© Copyright 2024</span>|<span>Lakeshore Grain Company</span>|<span>All Rights Reserved</span></div><div class="pg">16</div>
</section>

<!-- 18 Thank you -->
<section class="slide c3 r6 cover">
  <div class="photo" role="img" aria-label="Faded harvester field background" style="inset:0;background:radial-gradient(ellipse at 30% 80%,rgba(255,255,255,.07),transparent 60%)"></div>
  <div class="logo-box" style="left:42px;top:60px;width:98px;height:50px;font-size:9px">Lakeshore<br>Grain</div>
  <div class="abs" style="left:162px;top:45px;font-size:19px;font-weight:700;color:#fff">Thank You</div>
  <svg class="abs" style="left:162px;top:78px" width="10" height="60" viewBox="0 0 10 60">
    <path d="M2 2c0 4 3 7 6 7l1-2-2-1-1 1c-1 0-2-1-2-2l1-1-1-2z" fill="var(--red)"/>
    <path d="M1 27l8-3-3 8-1-3z" fill="var(--red)"/>
    <path d="M1 47l4-4 4 4h-1v4H2v-4z" fill="var(--red)"/>
  </svg>
  <div class="abs" style="left:175px;top:78px;width:1px;height:12px;background:#fff"></div>
  <div class="abs" style="left:175px;top:98px;width:1px;height:12px;background:#fff"></div>
  <div class="abs" style="left:175px;top:118px;width:1px;height:12px;background:#fff"></div>
  <div class="abs" style="left:180px;top:78px;font-size:5px;color:#fff;line-height:1.3">+18 2767 9470 1808<br>+18 2767 9470 1808</div>
  <div class="abs" style="left:180px;top:98px;font-size:5px;color:#fff;line-height:1.3">www.websitename.com<br>uname@email.com</div>
  <div class="abs" style="left:180px;top:118px;font-size:5px;color:#fff;line-height:1.3">1234 Street name, town/city,<br>state/country, post/zip 012345.</div>
</section>

</body>
</html>
```